Funeral Services Site

We need a website for a Funeral Services company. The old website is: www.rouwcentrumkorvelaer.be We need the same structure and text.

Target Market(s)

Customers.

Coding

Coded - Design and coding required

Number of Pages Required

4 page

Font styles to use
Serif
Sans Serif
Script

```html
<!DOCTYPE html>
<html lang="en">
<head>
<meta charset="utf-8">
<title>Funeral home Korvelaer bvba</title>
<link rel="stylesheet" href="https://fonts.googleapis.com/css2?family=Tinos:wght@400;700&family=Open+Sans:wght@400;600;700&display=swap">
<style>
:root{
  --ink:#222;
  --text:#3c3c3c;
  --muted:#777;
  --line:#cfcfcf;
  --dark:#1f1f1f;
  --btn:#3a3a3a;
  --white:#fff;
  --social:#6a6a6a;
}
*{box-sizing:border-box;margin:0;padding:0}
html,body{width:1200px;height:3727px;overflow:hidden}
body{position:relative;background:var(--white);font-family:"Tinos",serif;color:var(--text)}
.abs{position:absolute}
.serif{font-family:"Tinos",serif}
.sans{font-family:"Open Sans",sans-serif}

/* header */
.site-header{left:0;top:0;width:1200px;height:82px;background:var(--white);border-bottom:1px solid #e2e2e2}
.brand{left:130px;top:10px;display:flex;align-items:center;gap:12px}
.brand-mark{width:56px;height:56px;border-radius:50%;background:var(--dark)}
.brand-name{font-family:"Tinos",serif;font-weight:700;font-size:24px;line-height:26px;color:var(--ink)}
.header-tools{left:668px;top:26px;display:flex;gap:14px;align-items:center}
.pill{height:28px;border:1.5px solid #555;border-radius:14px;padding:0 12px;display:flex;align-items:center;gap:6px;font-family:"Open Sans",sans-serif;font-size:11px;font-weight:600;color:var(--ink)}
.menu-btn{width:30px;height:30px;border-radius:50%;background:var(--btn);display:flex;flex-direction:column;justify-content:center;align-items:center;gap:3px}
.menu-btn i{display:block;width:14px;height:2px;background:#fff}

/* hero */
.hero{left:0;top:82px;width:1200px;height:530px;overflow:hidden}
.hero-photo{position:absolute;inset:0;background:linear-gradient(100deg,#7a1a14 0%,#a3382a 22%,#6a3a22 38%,#b59a82 55%,#d8d2cc 72%,#8a8680 100%)}
.hero-copy{position:absolute;right:118px;top:168px;text-align:right;color:var(--white)}
.hero-title{font-size:38px;line-height:46px;letter-spacing:2px;text-transform:uppercase}
.hero-sub{font-size:21px;letter-spacing:1.5px;text-transform:uppercase;margin-top:6px}
.btn{display:inline-flex;align-items:center;gap:10px;height:40px;padding:0 20px 0 5px;border-radius:20px;background:var(--btn);color:#fff;font-family:"Tinos",serif;font-size:18px;letter-spacing:1px;text-transform:uppercase}
.btn .dot{width:30px;height:30px;border-radius:50%;border:1.5px solid #fff;display:flex;align-items:center;justify-content:center}
.hero .btn{margin-top:22px;background:rgba(40,40,40,.85)}
.hero-wave{position:absolute;left:0;bottom:0}

/* about */
.about-photo{left:137px;top:683px;width:260px;height:240px;border-radius:50%;background:radial-gradient(circle,#e8e8e8 0%,#bbb 70%,#222 72%,#222 100%)}
.about-copy{left:422px;top:695px;width:672px}
.sec-title{font-weight:400;font-size:23px;letter-spacing:1px;text-transform:uppercase;color:var(--ink);padding-bottom:8px;border-bottom:1px solid var(--line)}
.lead{font-weight:700;font-size:16px;margin:10px 0 4px;color:var(--ink)}
.body-text{font-size:14.5px;line-height:21px;color:var(--text)}
.body-text p+p{margin-top:18px}

/* organization */
.org{left:0;top:1006px;width:1200px;height:403px;background:linear-gradient(90deg,#ebebeb,#f3f3f3 60%,#ece6e8)}
.org-photo{left:119px;top:72px;width:353px;height:259px;background:linear-gradient(120deg,#2a2a35 0%,#6a6d74 45%,#c9ccc2 70%,#e8e8e4 100%)}
.org-copy{left:492px;top:72px;width:600px}
.org-copy .sec-title{border:0;padding-bottom:12px}
.bullets{list-style:none;margin-top:14px;font-size:14.5px;line-height:24px}
.bullets li::before{content:"›";margin-right:8px;font-weight:700}

/* section headings */
.section-head{left:0;width:1200px;text-align:center}
.section-head h2{font-weight:400;font-size:23px;letter-spacing:1px;text-transform:uppercase;color:var(--ink)}
.section-head .rule{margin:18px auto 0;width:960px;height:0;border-top:1px solid var(--line)}

/* condolences */
.cards{left:119px;top:1570px;width:962px;display:flex;justify-content:space-between}
.card{width:180px;text-align:center}
.card .portrait{width:180px;height:180px;border:1px solid #ddd;padding:6px;background:#fff}
.card .portrait div{width:100%;height:100%;background:linear-gradient(160deg,#9a7a6a,#5c4438)}
.card.light .portrait div{background:linear-gradient(160deg,#e8e4dc,#b8b0a4)}
.card .name{font-size:16px;line-height:19px;color:var(--ink);margin-top:14px}
.card .dates{font-size:11px;color:var(--muted);margin-top:4px}
.card.active{background:#f2f2f2}
.card .actions div{background:#4a4a4a;color:#eee;font-size:10.5px;height:22px;line-height:22px;text-align:left;padding-left:10px;border-bottom:1px solid #666}
.view-all{left:530px;top:1900px}
.view-all .btn{height:32px;font-size:15px}
.view-all .btn .dot{width:24px;height:24px}

/* cta */
.cta{left:0;top:2057px;width:1200px;height:321px;background:linear-gradient(90deg,#f4f4f6 0%,#e9ebef 55%,#d8dbe0 100%)}
.cta-text{left:144px;top:72px;width:450px;font-family:"Open Sans",sans-serif;font-weight:600;font-size:16px;line-height:29px;letter-spacing:1px;text-transform:uppercase;color:var(--ink)}
.cta .btn{left:144px;top:208px;height:32px;font-size:15px;font-family:"Open Sans",sans-serif;font-weight:600}
.cta .btn .dot{width:24px;height:24px}
.cta-flowers{left:720px;top:0;width:300px;height:321px;background:radial-gradient(ellipse at center,#f6f7f2 0%,#c9d2bd 45%,rgba(200,210,190,0) 72%)}

/* gallery */
.gallery{left:119px;top:2552px;width:962px;height:376px}
.g{position:absolute;border:1px solid #ddd;padding:5px;background:#fff}
.g div{width:100%;height:100%}

/* contact */
.contact-form{left:200px;top:3089px;width:800px}
.row{display:flex;gap:12px}
.field{flex:1;height:34px;border:1px solid #d6d6d6;font-size:13px;color:#999;padding:8px 10px}
.field.area{height:62px;margin-top:12px;flex:none;width:100%}
.submit{left:549px;top:3224px;width:102px;height:28px;border-radius:14px;background:var(--btn);color:#fff;font-family:"Tinos",serif;font-size:14px;letter-spacing:1px;text-align:center;line-height:28px}

/* footer */
.footer{left:0;top:3290px;width:1200px;height:437px}
.footer-bg{position:absolute;left:0;top:0}
.reach{position:absolute;left:160px;top:165px;width:880px}
.reach .track{position:absolute;left:90px;right:90px;top:38px;height:1px;background:#666}
.reach-item{position:absolute;top:0;width:300px;margin-left:-150px;text-align:center;color:#ddd;font-family:"Open Sans",sans-serif}
.reach-item .ico{width:36px;height:36px;border-radius:50%;border:1.5px solid #777;background:var(--dark);margin:6px auto 8px;display:flex;align-items:center;justify-content:center;position:relative}
.reach-item small{display:block;font-size:9px;letter-spacing:1px;color:#999}
.reach-item span{font-size:13px}
.socials{position:absolute;left:0;width:1200px;top:280px;display:flex;justify-content:center;gap:8px}
.socials i{width:24px;height:24px;border-radius:50%;background:var(--social)}
.foot-links{position:absolute;left:0;width:1200px;top:348px;text-align:center;font-family:"Open Sans",sans-serif;font-size:12px;color:#ddd}
.foot-links span{margin:0 10px}
.foot-links b{font-weight:400;color:#777}
.copyright{position:absolute;left:0;width:1200px;top:390px;text-align:center;font-family:"Open Sans",sans-serif;font-size:10px;color:#666}
</style>
</head>
<body>

<header class="site-header abs">
  <div class="brand abs">
    <span class="brand-mark"></span>
    <span class="brand-name">Funeral home<br>Korvelaer bvba</span>
  </div>
  <nav class="header-tools abs">
    <span class="pill">
      <svg width="12" height="12" viewBox="0 0 24 24"><path d="M6 2h4l2 5-3 2a12 12 0 0 0 6 6l2-3 5 2v4a2 2 0 0 1-2 2A18 18 0 0 1 4 4a2 2 0 0 1 2-2z" fill="#333"/></svg>
      011 70 38 38</span>
    <span class="pill">
      <svg width="12" height="12" viewBox="0 0 24 24"><circle cx="12" cy="10" r="6" fill="none" stroke="#333" stroke-width="2"/><path d="M12 16v6" stroke="#333" stroke-width="2"/></svg>
      SEND FLOWERS</span>
    <span class="pill">ENGLISH ▾</span>
    <span class="menu-btn"><i></i><i></i><i></i></span>
  </nav>
</header>

<section class="hero abs">
  <div class="hero-photo" role="img" aria-label="Red roses lying on a wooden coffin with a hand resting on it"></div>
  <div class="hero-copy">
    <div class="hero-title">Funeral home<br>Korvelaer bvba</div>
    <div class="hero-sub">A personal service in farewell guidance</div>
    <span class="btn"><span class="dot"><svg width="14" height="14" viewBox="0 0 24 24"><path d="M6 2h4l2 5-3 2a12 12 0 0 0 6 6l2-3 5 2v4a2 2 0 0 1-2 2A18 18 0 0 1 4 4a2 2 0 0 1 2-2z" fill="#fff"/></svg></span>Contact us</span>
  </div>
  <svg class="hero-wave" width="1200" height="140" viewBox="0 0 1200 140" preserveAspectRatio="none">
    <path d="M0 120 C250 150 520 110 760 70 C950 38 1100 20 1200 10 L1200 140 L0 140 Z" fill="#fff"/>
    <path d="M0 118 C250 146 520 106 760 66 C950 34 1100 16 1200 6" fill="none" stroke="#2a2a2a" stroke-width="7" opacity=".85"/>
  </svg>
</section>

<div class="about-photo abs" role="img" aria-label="Drawing of a grieving figure kneeling, in a round frame"></div>
<section class="about-copy abs">
  <h2 class="sec-title">About us</h2>
  <p class="lead">Mourning center Korvelaer, a complete service in mourning and farewell guidance</p>
  <div class="body-text">
    <p>Saying goodbye to a loved one is one of the toughest things in a lifetime. Funeral home Korvelaer in Heidebeek takes care of all the practical and administrative matters involved. So you can say goodbye in peace.</p>
    <p>Our people have a long experience in farewell guidance and stand for 24 hours at 24 hours for you. Our fully renovated funeral home is open to you and your acquaintances, so that you can greet your loved one at any time of the day.</p>
  </div>
</section>

<section class="org abs">
  <div class="org-photo abs" role="img" aria-label="Lit candle beside a coffin with white flowers"></div>
  <div class="org-copy abs">
    <h2 class="sec-title">Organization funeral and worship</h2>
    <div class="body-text">
      <p>The organization of the funeral ceremony is a moment of reflection, where the personality of the deceased can be beautifully highlighted. Our team will assist you in this and select the most beautiful texts, songs and photos with you in order to arrive at an appropriate and worthy goodbye.</p>
      <p>The funeral can take place in your parish church or our auditorium if you wish, which can accommodate a maximum of 100 guests. We can arrange the following for you:</p>
    </div>
    <ul class="bullets">
      <li>Vigil the night before the funeral</li>
      <li>Prayer service with priest (if possible)</li>
      <li>Eucharistic celebration with priest (on Tuesday and Friday in the parishes of Heidebeek)</li>
    </ul>
  </div>
</section>

<div class="section-head abs" style="top:1476px">
  <h2>Condole online</h2>
  <div class="rule"></div>
</div>
<div class="cards abs">
  <div class="card"><div class="portrait"><div role="img" aria-label="Portrait of the deceased"></div></div><div class="name">Gerard Aloys<br>Vandeput</div><div class="dates">05 maart 1931 - 02 mei 2019</div></div>
  <div class="card light"><div class="portrait"><div role="img" aria-label="Portrait of the deceased"></div></div><div class="name">Maria<br>Claessen</div><div class="dates">20 juli 1936 - 29 april 2019</div></div>
  <div class="card light active"><div class="portrait"><div role="img" aria-label="Portrait of the deceased"></div></div><div class="name">Rita Lemmens</div><div class="dates">30 maart 1949 - 04 mei 2019</div>
    <div class="actions sans" style="margin-top:8px"><div>Download Rouwbrief</div><div>Bloemen bestellen</div></div></div>
  <div class="card"><div class="portrait"><div role="img" aria-label="Portrait of the deceased"></div></div><div class="name">Paul<br>Geukens</div><div class="dates">05 maart 1931 - 02 mei 2019</div></div>
  <div class="card"><div class="portrait"><div role="img" aria-label="Photo of the deceased with a motorcycle" style="background:linear-gradient(160deg,#7a1a1a,#c23a2a 50%,#3a3a3a)"></div></div><div class="name">Frans "Sjef"<br>Moonen</div><div class="dates">05 maart 1931 - 02 mei 2019</div></div>
</div>
<div class="view-all abs"><span class="btn"><span class="dot"><svg width="10" height="10" viewBox="0 0 10 10"><path d="M3 1l4 4-4 4" fill="none" stroke="#fff" stroke-width="1.5"/></svg></span>View all</span></div>

<section class="cta abs">
  <p class="cta-text abs">Do you have any questions or would you like to call in our funeral home? Contact us. We are here for you.</p>
  <span class="btn abs"><span class="dot"><svg width="12" height="12" viewBox="0 0 24 24"><path d="M6 2h4l2 5-3 2a12 12 0 0 0 6 6l2-3 5 2v4a2 2 0 0 1-2 2A18 18 0 0 1 4 4a2 2 0 0 1 2-2z" fill="#fff"/></svg></span>Contact us</span>
  <div class="cta-flowers abs" role="img" aria-label="Arrangement of white lilies and roses"></div>
</section>

<div class="section-head abs" style="top:2445px">
  <h2>Gallery</h2>
  <div class="rule"></div>
</div>
<div class="gallery abs">
  <div class="g" style="left:0;top:0;width:300px;height:172px"><div role="img" aria-label="Red rose on a white cloth" style="background:linear-gradient(135deg,#d6d8dc,#f2f2f2 60%,#8d2a22)"></div></div>
  <div class="g" style="left:330px;top:0;width:300px;height:376px"><div role="img" aria-label="Funeral wreath of white flowers on a stand" style="background:radial-gradient(circle,#f4f4ee 0%,#b9c7a6 55%,#e6e6e6 80%)"></div></div>
  <div class="g" style="left:662px;top:0;width:300px;height:172px"><div role="img" aria-label="White lily beside a candle" style="background:linear-gradient(135deg,#3a3a3a,#e8e6d8 55%,#5a5a5a)"></div></div>
  <div class="g" style="left:0;top:198px;width:300px;height:178px"><div role="img" aria-label="Hand holding a white lily" style="background:linear-gradient(135deg,#4a3020,#d8b890 50%,#2a2220)"></div></div>
  <div class="g" style="left:662px;top:198px;width:300px;height:178px"><div role="img" aria-label="Spray of white roses" style="background:linear-gradient(135deg,#a8a0a4,#f0eeea 55%,#7e8a6c)"></div></div>
</div>

<div class="section-head abs" style="top:2975px">
  <h2>Contact us</h2>
  <div class="rule"></div>
</div>
<form class="contact-form abs">
  <div class="row"><div class="field">Name:</div><div class="field">Phone:</div><div class="field">Mail</div></div>
  <div class="field area">Comment</div>
</form>
<div class="submit abs">SUBMIT</div>

<footer class="footer abs">
  <svg class="footer-bg" width="1200" height="437" viewBox="0 0 1200 437" preserveAspectRatio="none">
    <path d="M0 100 C300 110 600 40 900 20 C1030 12 1120 8 1200 0 L1200 437 L0 437 Z" fill="#1f1f1f"/>
    <path d="M0 96 C300 106 600 36 900 16 C1030 8 1120 4 1200 -4" fill="none" stroke="#444" stroke-width="4"/>
  </svg>
  <div class="reach">
    <div class="track"></div>
    <div class="reach-item" style="left:90px"><small>CALL US</small><div class="ico"><svg width="14" height="14" viewBox="0 0 24 24"><path d="M6 2h4l2 5-3 2a12 12 0 0 0 6 6l2-3 5 2v4a2 2 0 0 1-2 2A18 18 0 0 1 4 4a2 2 0 0 1 2-2z" fill="#ccc"/></svg></div><span>011 70 38 38</span></div>
    <div class="reach-item" style="left:440px"><small>MAIL US</small><div class="ico"><svg width="16" height="12" viewBox="0 0 16 12"><rect x="1" y="1" width="14" height="10" fill="none" stroke="#ccc"/><path d="M1 1l7 6 7-6" fill="none" stroke="#ccc"/></svg></div><span>info@rouwcentrumkorvelaer.be</span></div>
    <div class="reach-item" style="left:790px"><small>LOCATION</small><div class="ico"><svg width="12" height="16" viewBox="0 0 12 16"><path d="M6 15C2 10 1 8 1 6a5 5 0 0 1 10 0c0 2-1 4-5 9z" fill="none" stroke="#ccc"/><circle cx="6" cy="6" r="2" fill="#ccc"/></svg></div><span>Lindeweg 18, 3770 Heidebeek</span></div>
  </div>
  <div class="socials"><i></i><i></i><i></i><i></i><i></i></div>
  <div class="foot-links"><span>Home</span><b>|</b><span>About us</span><b>|</b><span>Condole online</span><b>|</b><span>Order flowers</span><b>|</b><span>Contact</span><b>|</b><span>Sitemap</span><b>|</b><span>Privacy Policy</span></div>
  <div class="copyright">Copyright © 2016 Lumen Web Studio. All Rights reserved.</div>
</footer>

</body>
</html>
```